VelmorDrops (Foundational) Product Label

Ok. Soooo...I have a "high-end" hair nourishing/care product line that needs a "foundational" label - slightly alerted for various formulas. My products are all natural and do not contain artificial ingredients or preservatives and will need a label that will attract multicultural consumers that want gentle, caring products.

What am I looking for? Good question! I just know that I'm looking an elegant, yet creative, colorful, modern label that will look fabulous especially on Tavrel Glass 30 and 50 ml pipette bottles. (Please Google it since I can't add links to this brief.)

Additionally, I have two logos that need adding to the bottle, which can be emailed to you. I'll need to be able to add a barcode and list of ingredients to the label...most of which are proprietary blends and will most likely by listed as such.

As I've told other designers, I don't always know what I want, but will know it when I see it. I hope to closeout this project within 15 days (I added time to travel for a wedding and may not respond as quickly as I may want).

Thank you for your interest and I look forward to seeing your creations!!
Updates

Please add "SHAKE WELL. Product may separate." immediately after the words "Recommended use:".

Target Market(s)

Unisex, multicultural, consumers with natural or processed hair.

Industry/Entity Type

Hair

Font styles to use
Script

Requirements
Must have
• Some color...I like natural and neutral colors, but want splashes of color that pop.
• Label details:
• I've already uploaded the logos to the project brief. You have my permission to refine/change the logos to meet your creative design. The "(TM)" is for the "trademark symbol"
• Product: VelmorDrops(TM) by QuindaloGraced(TM) Nourishing Hair and Scalp Oil Blend
• Unit: 50 mL
• PRECAUTIONS: FOR EXTERNAL USE ONLY. If ingested contact your local Poison Control Office. Keep away from open flames. Avoid direct sunlight. Keep out of reach of children. Consult a physician if pregnant.
• Ingredients: Cocos nucifera (Coconut Oil), Olea europaea L. (Extra Virgin Olive Oil), Ricinus Communis (Castor Oil), Vitis vinifera L. (Grapeseed Oil), Butyrospermum parkii (Shea Butter),  Carthamus tinctorius L. (Safflower Oil),  Prunus dulcis (Sweet Almond Oil), and other ingredients.
• Recommended use: Apply sparingly to clean scalp and hair and gently massage. Style as usual. A little goes a long way so repeat application only as needed to avoid saturation.
• For additional information please visit www.VelmorDrops.example or email us at
• Info@VelmorDrops.example
• Created and Distributed by:
• Loretta Brimsby-Kane Ventures, LLC, Halbrook, VA 20917
• (855) 307-4192
Nice to have
• I THINK I would like to see pictures of Shea, coconuts, olives, open grapes showing the seeds...something to help tell the story about the all-natural ingredients. As for the font, I do like script styles, but the packaging isn't for me...nor has to attract me...so I need fonts, colors, and a layout that will attract both women AND men.
Should not have
• I don't want pictures of models, or people or anything that could steer the products from one culture to another. Anyone with skin and/or hair can use my oils (and bath minerals).

```html
<!DOCTYPE html>
<html lang="en">
<head>
<meta charset="utf-8">
<title>VelmorDrops Nourishing Hair and Scalp Oil Blend – Label</title>
<link rel="stylesheet" href="https://fonts.googleapis.com/css2?family=Open+Sans:ital,wght@0,400;0,600;0,700;1,400&family=Crimson+Text:wght@400;600&display=swap">
<style>
  :root {
    --page: #eeeeee;
    --label-top: #ffffff;
    --label-bottom: #e9eee8;
    --ink: #1b1b1b;
    --green: #3f7a2e;
    --green-dark: #2d6327;
    --green-light: #7fcf5a;
    --olive-a: #a9c94a;
    --olive-b: #5f8f2b;
    --charcoal: #2a2a2a;
    --white: #ffffff;
  }
  * { box-sizing: border-box; margin: 0; padding: 0; }
  html, body { width: 973px; height: 1200px; overflow: hidden; }
  body {
    background: var(--page);
    font-family: "Open Sans", Arial, sans-serif;
    color: var(--ink);
    position: relative;
  }
  .label {
    position: absolute;
    left: 36px; top: 309px;
    width: 900px; height: 582px;
    background: linear-gradient(180deg, var(--label-top) 40%, var(--label-bottom) 100%);
    box-shadow: 0 2px 10px rgba(0,0,0,.25);
    overflow: hidden;
  }
  .column-left {
    position: absolute; left: 15px; top: 28px; width: 300px;
    font-size: 15.5px; line-height: 1.42;
  }
  .heading { color: var(--green); font-weight: 700; }
  .ingredients { margin-bottom: 22px; }
  .usage-title { display: block; font-size: 15.5px; text-transform: uppercase; }
  .shake-well {
    margin-top: 18px; color: var(--green); font-weight: 700; font-size: 17px;
  }
  .recycle-icon { position: absolute; left: 40px; top: 445px; width: 44px; height: 44px; }

  .column-center {
    position: absolute; left: 310px; top: 0; width: 290px; text-align: center;
  }
  .company-mark {
    margin: 30px auto 0; width: 168px; height: 78px; border-radius: 50%;
    background: var(--charcoal); color: var(--white);
    display: flex; align-items: center; justify-content: center;
    font-family: "Open Sans", Arial, sans-serif; font-size: 11px; font-weight: 600;
    line-height: 1.25; padding: 0 16px;
  }
  .brand-name {
    margin-top: 52px;
    font-family: "Crimson Text", Georgia, serif; font-weight: 600;
    font-size: 46px; color: var(--green); line-height: 1;
  }
  .brand-by {
    font-family: "Crimson Text", Georgia, serif; font-size: 13px;
    color: var(--green); letter-spacing: .08em; margin-top: 2px;
  }
  .olive-art {
    margin: 20px auto 0; width: 190px; height: 160px; border-radius: 50%;
    background: radial-gradient(circle at 55% 60%, var(--olive-a) 0%, var(--olive-b) 45%, rgba(255,255,255,0) 72%);
  }
  .product-name {
    margin-top: 12px;
    font-family: "Crimson Text", Georgia, serif; font-size: 25px; line-height: 1.15;
    color: var(--ink);
  }

  .column-right {
    position: absolute; left: 612px; top: 28px; width: 280px;
    font-size: 15.5px; line-height: 1.42;
  }
  .precautions-title { display: block; text-transform: uppercase; }
  .contact {
    margin-top: 52px; text-align: center; font-size: 14px; line-height: 1.5;
  }
  .contact em { font-style: italic; }
  .contact strong { font-weight: 700; }
  .company-mark.small {
    margin: 16px auto 0; width: 76px; height: 40px; font-size: 6px; padding: 0 6px;
    background: var(--white); color: var(--charcoal); border: 2px solid var(--charcoal);
  }
  .distributor { margin-top: 14px; text-align: center; font-size: 14.5px; line-height: 1.4; }

  .band-line {
    position: absolute; left: 0; right: 0; top: 492px; height: 6px; background: var(--green-light);
  }
  .band {
    position: absolute; left: 0; right: 0; top: 498px; bottom: 0;
    background: var(--green-dark); color: var(--white);
    display: flex; align-items: center; justify-content: center;
    font-size: 28px; font-weight: 700;
  }
</style>
</head>
<body>
  <main class="label">
    <section class="column-left">
      <p class="ingredients"><span class="heading">Ingredients:</span> Cocos nucifera (Coconut Oil), Olea europaea L. (Extra Virgin Olive Oil), Ricinus Communis (Castor Oil), Vitis vinifera L. (Grapeseed Oil), Butyrospermum parkii (Shea Butter), Carthamus tinctorius L. (Safflower Oil), Prunus dulcis (Sweet Almond Oil), and other ingredients.</p>
      <p><span class="heading usage-title">Recommended use:</span>Apply sparingly to clean scalp and hair and gently massage. Style as usual. A little goes a long way so repeat application only as needed to avoid saturation.</p>
      <p class="shake-well">SHAKE WELL</p>
    </section>

    <svg class="recycle-icon" viewBox="0 0 44 44" aria-label="Recyclable">
      <g fill="none" stroke="#1b1b1b" stroke-width="4" stroke-linejoin="round">
        <path d="M16 10 L22 2 L28 10"/>
        <path d="M36 20 L40 30 L30 34"/>
        <path d="M14 36 L4 32 L10 22"/>
      </g>
      <g fill="#1b1b1b">
        <polygon points="24,4 34,18 28,20"/>
        <polygon points="36,36 16,38 20,32"/>
        <polygon points="6,28 14,10 18,16"/>
      </g>
    </svg>

    <section class="column-center">
      <div class="company-mark">Loretta Brimsby-Kane Ventures</div>
      <h1 class="brand-name">VelmorDrops</h1>
      <p class="brand-by">by QuindaloGraced®</p>
      <div class="olive-art" role="img" aria-label="Illustration of an olive branch with green olives and leaves"></div>
      <h2 class="product-name">Nourishing Hair and<br>Scalp Oil Blend</h2>
    </section>

    <section class="column-right">
      <p><span class="heading precautions-title">Precautions:</span>FOR EXTERNAL USE ONLY. If ingested contact your local Poison Control Office. Keep away from open flames. Avoid direct sunlight. Keep out of reach of children. Consult a physician if pregnant.</p>
      <div class="contact">
        <p><em>For additional information please visit</em></p>
        <p><strong>www.VelmorDrops.example</strong></p>
        <p><em>or email us at</em></p>
        <p><strong>Info@VelmorDrops.example</strong></p>
      </div>
      <div class="company-mark small">Loretta Brimsby-Kane</div>
      <p class="distributor">Distributed by:<br>Loretta Brimsby-Kane Ventures,<br>LLC Halbrook, VA 20917<br>(855) 307-4192</p>
    </section>

    <div class="band-line"></div>
    <div class="band">50 mL</div>
  </main>
</body>
</html>
```